Cleaning Company Banner

Looking to have a Banner made that shows our contact information and shows what we do with good imagery to catch cars driving by. Will be a 6' x 3' banner (landscape). Attached our logo and flyer that we currently hand out.

```html
<!DOCTYPE html>
<html lang="en">
<head>
<meta charset="utf-8">
<title>BrightWay Cleaning Banner</title>
<link href="https://fonts.googleapis.com/css2?family=League+Spartan:wght@700;800&family=Montserrat:ital,wght@0,800;1,400;1,900&display=swap" rel="stylesheet">
<style>
  :root {
    --teal-deep: #0a5f7a;
    --teal-mid: #1287a8;
    --band: #5fc3dc;
    --frame: #5ccbe4;
    --headline: #0b3f52;
    --white: #ffffff;
    --yellow: #ffcc00;
    --ink: #0a2431;
  }
  html, body { margin: 0; padding: 0; overflow: hidden; }
  body { width: 1200px; height: 600px; }
  .banner {
    position: relative;
    width: 1200px;
    height: 600px;
    overflow: hidden;
    background: linear-gradient(120deg, #3aa0bd 0%, var(--teal-mid) 35%, var(--teal-deep) 75%, #0b6c88 100%);
    font-family: "League Spartan", sans-serif;
  }
  .shapes { position: absolute; inset: 0; }
  .headline {
    position: absolute;
    left: 20px;
    top: 19px;
    margin: 0;
    font-family: "Montserrat", sans-serif;
    font-weight: 900;
    font-style: italic;
    font-size: 33px;
    line-height: 41px;
    color: var(--headline);
    white-space: nowrap;
  }
  .services {
    position: absolute;
    left: 20px;
    top: 129px;
    color: var(--white);
    font-weight: 700;
  }
  .services h2 { margin: 0 0 4px; font-size: 38px; line-height: 38px; }
  .services ul { list-style: none; margin: 0; padding: 0; }
  .services li { font-size: 52px; line-height: 51px; white-space: nowrap; }
  .cta {
    position: absolute;
    left: 0;
    width: 726px;
    top: 397px;
    text-align: center;
    margin: 0;
    color: var(--yellow);
    font-size: 42px;
    line-height: 44px;
    font-weight: 800;
    letter-spacing: 0.5px;
  }
  .phone {
    position: absolute;
    left: 14px;
    top: 438px;
    margin: 0;
    color: var(--yellow);
    font-family: "Montserrat", sans-serif;
    font-weight: 800;
    font-size: 86px;
    line-height: 90px;
    white-space: nowrap;
  }
  .contact {
    position: absolute;
    left: 0;
    width: 804px;
    top: 527px;
    text-align: center;
    margin: 0;
    color: var(--ink);
    font-family: "Montserrat", sans-serif;
    font-style: italic;
    font-size: 28px;
    line-height: 31px;
    white-space: nowrap;
  }
  .brand-name {
    position: absolute;
    left: 930px;
    top: 100px;
    width: 250px;
    text-align: center;
    color: var(--white);
    font-weight: 700;
    font-size: 36px;
    line-height: 36px;
    margin: 0;
  }
</style>
</head>
<body>
<div class="banner">
  <svg class="shapes" width="1200" height="600" viewBox="0 0 1200 600">
    <defs>
      <linearGradient id="cornerGlow" x1="0" y1="0" x2="1" y2="1">
        <stop offset="0" stop-color="#1b9ec2"/>
        <stop offset="1" stop-color="#0d7fa1"/>
      </linearGradient>
      <linearGradient id="roomTone" x1="0" y1="0" x2="1" y2="1">
        <stop offset="0" stop-color="#c9b49a"/>
        <stop offset="0.45" stop-color="#e8e0d5"/>
        <stop offset="0.75" stop-color="#b9b1a9"/>
        <stop offset="1" stop-color="#a88c6c"/>
      </linearGradient>
      <linearGradient id="floorTone" x1="0" y1="0" x2="1" y2="1">
        <stop offset="0" stop-color="#e9ecee"/>
        <stop offset="0.6" stop-color="#c7d3d8"/>
        <stop offset="1" stop-color="#e6c23a"/>
      </linearGradient>
    </defs>
    <polygon class="corner-panel" points="885,0 1200,0 1200,600 900,600" fill="url(#cornerGlow)"/>
    <polygon class="headline-band" points="0,0 883,0 927,110 0,110" fill="var(--band)" opacity="0.75"/>
    <polygon class="photo-frame" points="890,168 1200,168 1200,600 786,600 727,427" fill="var(--frame)"/>
    <polygon class="photo-main" role="img" aria-label="Photo of two cleaners in aprons and gloves wiping a television and vacuuming a living room"
      points="897,176 1200,176 1200,600 794,600 737,427" fill="url(#roomTone)"/>
    <polygon class="hex-frame" points="673,177 722,90 823,90 872,177 823,264 722,264" fill="var(--frame)"/>
    <polygon class="photo-hex" role="img" aria-label="Photo of a mop on a shiny floor and yellow gloves on a bucket"
      points="681,177 726,98 819,98 864,177 819,256 726,256" fill="url(#floorTone)"/>
  </svg>

  <h1 class="headline">QUALITY DRIVEN AND RELIABLE TO TAKE CARE<br>OF ALL YOUR CLEANING NEEDS!!!</h1>

  <section class="services">
    <h2>SERVICES:</h2>
    <ul>
      <li>RESIDENTIAL CLEANING</li>
      <li>COMMERCIAL CLEANING</li>
      <li>ANTIVIRAL DISINFECTION</li>
      <li>CONSTRUCTION CLEANING</li>
    </ul>
  </section>

  <p class="cta">CALL OR TEXT:</p>
  <p class="phone">(555) 014 - 2768</p>
  <p class="contact">Dana Whitfield - Owner/operator<br>thebrightwayclean@mail.com</p>

  <p class="brand-name">BRIGHTWAY<br>CLEANING</p>
</div>
</body>
</html>
```